Corporate Profile

We are an Electrical Engineering company and we require a rework on our company profile urgently. We need it be have a nice modern look and feel.

We do not have much time as we need the brochures ready printed before 24th Oct 2014.

Please find attached a .pdf file with our company profile and a complimetary slip that has our high definition logo to be extracted.

1. We require a front page design. 2. There is no particular size. You can suggest on the size.

Electrical

```html
<!DOCTYPE html>
<html lang="en">
<head>
<meta charset="utf-8">
<title>Volt Crest – Company Profile</title>
<link rel="stylesheet" href="https://fonts.googleapis.com/css2?family=Arimo:wght@400;700&family=Roboto+Condensed:wght@400;700&display=swap">
<style>
:root{
  --backdrop:#6b6b6b;
  --paper:#ffffff;
  --red:#e0001b;
  --ink:#2b2b2b;
  --body:#333333;
  --rule:#e4e4e4;
  --panel-top:#ffffff;
  --panel-bottom:#e5e5e5;
}
*{margin:0;padding:0;box-sizing:border-box}
html,body{width:998px;height:1200px;overflow:hidden;background:var(--backdrop)}
.page{position:absolute;left:93px;top:76px;width:811px;height:1048px;background:var(--paper);font-family:"Arimo",Arial,sans-serif;color:var(--body)}
.side-panel{position:absolute;left:0;top:160px;width:318px;height:888px;background:linear-gradient(to bottom,var(--panel-top) 0%,var(--panel-top) 25%,var(--panel-bottom) 100%)}
.brand{position:absolute;left:60px;top:36px;display:flex;align-items:center;gap:10px}
.brand-dot{width:34px;height:34px;border-radius:50%;background:var(--red)}
.brand-name{font-family:"Arimo",Arial,sans-serif;font-weight:700;font-size:17px;color:var(--red);letter-spacing:.5px;text-transform:uppercase;line-height:1}
.rule{position:absolute;height:6px;background:var(--rule)}
.heading{position:absolute;color:var(--red);font-weight:700}
.heading-lg{font-size:26px}
.heading-sm{font-size:18.5px}
.lead{position:absolute;left:57px;width:250px;font-size:18.3px;line-height:24.3px;color:var(--ink)}
.copy{position:absolute;left:351px;width:420px;font-size:12.4px;line-height:17.6px}
.product{position:absolute;left:351px;width:420px;font-size:12.4px;line-height:17.6px}
.product h4{font-size:12.4px;font-weight:700;color:var(--ink)}
.product h4 span{display:inline-block;width:22px}
.product p{padding-left:27px;margin-bottom:6px}
.areas{display:grid;grid-template-columns:1fr 1fr;padding-left:27px;list-style:none;line-height:16px}
.areas li{position:relative;padding-left:24px}
.areas li::before{content:"";position:absolute;left:4px;top:6px;width:5px;height:5px;border-radius:50%;background:var(--ink)}
.footer-band{position:absolute;left:0;top:973px;width:811px;height:56px;background:var(--red);display:flex;align-items:center;justify-content:flex-end;padding-right:118px}
.footer-label{font-family:"Roboto Condensed",Arial,sans-serif;font-size:18.5px;color:#fff;letter-spacing:.2px}
.footer-label b{font-weight:700;margin-left:8px}
.footer-label .sep{margin-left:8px;font-weight:700}
</style>
</head>
<body>
<div class="page">
  <div class="side-panel"></div>

  <div class="brand">
    <span class="brand-dot"></span>
    <span class="brand-name">Volt Crest</span>
  </div>

  <div class="rule" style="left:28px;top:157px;width:97px"></div>
  <h2 class="heading heading-lg" style="left:57px;top:171px">Vision</h2>
  <p class="lead" style="top:206px">To be a leading company in providing electrical energy efficiency solutions by the year 2030.</p>

  <div class="rule" style="left:28px;top:348px;width:116px"></div>
  <h2 class="heading heading-lg" style="left:57px;top:360px">Mission</h2>
  <p class="lead" style="top:393px">To spread out our market throughout Africa, both in market share and reputation, while providing maximum return on investment. Our Focus is providing general electrical solutions for domestic, commercial and industrial consumers and also utility providers. Volt Crest will achieve its goals by carefully understanding and meeting the needs of our overall market and offering the benefits of proven advance technologies that suits the market. We will transform our customers' efficiency and productivity to sustainable world-class standards.</p>

  <div class="rule" style="left:319px;top:156px;width:92px"></div>
  <h3 class="heading heading-sm" style="left:351px;top:172px">History</h3>
  <p class="copy" style="top:201px">Volt Crest started as an electrical product sales company in 1991. Volt Crest has evolved to be a complete electrical engineering company with its offices in Riverside district, Kisumu, Kenya. Volt Crest deals in a broad range of electrical products for domestic, commercial and industrial applications. Volt Crest has also over the years become a major solution provider for industries, commercial and domestic setups by helping them identify various ways of cutting costs through the saving of energy. Through conducting comprehensive Power Quality Analysis (PQA) and Energy Audits we are able to advice our customers on the various ways to reduce their power quality problems and the various energy saving opportunities available to them therefore helping them improve their overall efficiency. Since inception Volt Crest has built a strong engineering team that has well established knowledge in the electrical engineering field and is able to apply its knowledge to the actual situation. Volt Crest has a well established market throughout Kenya for 20 years since its inception.</p>

  <div class="rule" style="left:319px;top:521px;width:92px"></div>
  <h3 class="heading heading-sm" style="left:351px;top:537px">Products</h3>
  <p class="copy" style="top:567px">Volt Crest deals in various products within the electrical scope that helps companies maximize their output production. This ranges from Solutions to products. Some of our products are as below:</p>

  <div class="product" style="top:626px">
    <h4><span>1.</span>Power Quality</h4>
    <p>Due to increase in more electronic and other sensitive equipments in our industries there is need to have to have clean supply of electrical power to ensure there is minimum production downtimes due to machine breakdowns as a result of poor Quality of Power.</p>
    <p>Volt Crest helps domestic and industrial setups know their power quality status and help them to improve where required. This done by the help of Power Quality Analyzer which collects analyses and stores various electrical data which is then used by the electrical engineers to provide improvement solutions. Some of the areas monitored are:</p>
    <ul class="areas">
      <li>Transients</li><li>Interruptions</li>
      <li>Surges</li><li>Flicker</li>
      <li>Harmonics</li><li>Unbalance</li>
      <li>Dips and Swells</li><li>Under / Over Voltages</li>
    </ul>
  </div>

  <div class="footer-band">
    <span class="footer-label">COMPANY PROFILE<span class="sep">|</span><b>01</b></span>
  </div>
</div>
</body>
</html>
```